Business Card Design Competition

We need a business card design for our Internet Marketing company. We require both front and back designs and the final card must be 89x53mm in size, plus crop marks to 91x55mm. Colours as per logo, plus perhaps black and/or grey (#828282).
Final text must be editable (if you can supply an editable Fireworks PNG, even better)...
FRONT TEXT:
Full Name
Position
Address Line
Suburb, State, Postcode
Phone: 0000 000 000
Mobile: 0000 000 000
Email: xxx@brindlereach.com.au
Web: www.brindlereach.com.au
Rear of card should be a fresh design plus our slogan text: "Making You Visible" in large font, then in small text "Brindle Harbour Pty Ltd (ABN: 42 356 701 483)".

```html
<!DOCTYPE html>
<html lang="en">
<head>
<meta charset="utf-8">
<title>Brindle Reach – Business Card</title>
<link rel="stylesheet" href="https://fonts.googleapis.com/css2?family=Michroma&family=Open+Sans:wght@400;600&display=swap">
<style>
  :root {
    --green: #8cc63f;
    --green-light: #a9d33a;
    --green-dark: #76b531;
    --orange: #f7a021;
    --black: #151515;
    --charcoal: #2c2c2c;
    --grey: #828282;
    --white: #ffffff;
    --backdrop: #e9e6e1;
  }
  * { margin: 0; padding: 0; box-sizing: border-box; }
  html, body { width: 1200px; height: 771px; overflow: hidden; }
  body {
    background: var(--backdrop);
    font-family: "Open Sans", Arial, sans-serif;
    position: relative;
  }
  .card {
    position: absolute;
    overflow: hidden;
    box-shadow: 0 6px 18px rgba(0,0,0,0.25);
  }
  .card svg.card-art { position: absolute; inset: 0; }

  /* Front card */
  .card-front { left: 40px; top: 66px; width: 380px; height: 638px; }
  .front-name {
    position: absolute; right: 20px; top: 44px;
    font-family: "Michroma", sans-serif; font-size: 32px;
    color: var(--black); white-space: nowrap;
  }
  .front-position {
    position: absolute; right: 22px; top: 96px;
    font-family: "Michroma", sans-serif; font-size: 21px;
    color: var(--white); white-space: nowrap;
  }
  .front-phones { position: absolute; left: 28px; top: 232px; }
  .phone-row {
    display: flex; align-items: center; gap: 10px;
    font-size: 21px; color: var(--charcoal); height: 42px;
  }
  .phone-row svg { width: 24px; height: 24px; }
  .phone-divider {
    position: absolute; left: 268px; top: 226px;
    width: 1px; height: 100px; background: var(--green-dark);
  }
  .front-web {
    position: absolute; left: 28px; top: 388px;
    font-size: 17px; line-height: 26px; color: var(--white); white-space: nowrap;
  }
  .front-brand {
    position: absolute; left: 26px; top: 506px;
    display: flex; align-items: center; gap: 14px;
  }
  .brand-dot { width: 62px; height: 62px; border-radius: 50%; background: var(--orange); flex: none; }
  .brand-name {
    font-family: "Michroma", sans-serif; color: var(--orange);
    font-size: 29px; line-height: 34px; white-space: nowrap;
  }
  .front-address {
    position: absolute; left: 30px; top: 598px;
    display: flex; align-items: center; gap: 8px;
    font-size: 14px; color: var(--grey); white-space: nowrap;
  }
  .front-address svg { width: 14px; height: 18px; }

  /* Back card */
  .card-back { left: 460px; top: 177px; width: 700px; height: 417px; background: var(--black); }
  .back-brand {
    position: absolute; left: 42px; top: 66px;
    display: flex; align-items: center; gap: 26px;
  }
  .back-brand .brand-dot { width: 160px; height: 160px; }
  .back-brand .brand-name { font-size: 54px; line-height: 70px; }
  .back-slogan {
    position: absolute; left: 150px; top: 266px;
    font-family: "Michroma", sans-serif; font-size: 30px; color: var(--white); white-space: nowrap;
  }
  .back-legal {
    position: absolute; left: 186px; top: 314px;
    font-size: 14px; color: var(--grey); letter-spacing: 0.3px; white-space: nowrap;
  }
</style>
</head>
<body>

<section class="card card-front" aria-label="Card front">
  <svg class="card-art" width="380" height="638" viewBox="0 0 380 638">
    <defs>
      <radialGradient id="front-glow" cx="0.6" cy="0.4" r="0.8">
        <stop offset="0" stop-color="#a9d33a"/>
        <stop offset="1" stop-color="#8cc63f"/>
      </radialGradient>
      <radialGradient id="front-dark" cx="0.4" cy="0.4" r="0.8">
        <stop offset="0" stop-color="#3a3a3a"/>
        <stop offset="1" stop-color="#151515"/>
      </radialGradient>
    </defs>
    <rect width="380" height="638" fill="url(#front-glow)"/>
    <rect width="380" height="20" fill="#151515"/>
    <polygon points="0,452 380,478 380,638 0,638" fill="url(#front-dark)"/>
  </svg>

  <div class="front-name">Full Name</div>
  <div class="front-position">Position</div>

  <div class="front-phones">
    <div class="phone-row">
      <svg viewBox="0 0 24 24"><circle cx="12" cy="12" r="10.5" fill="none" stroke="#2c2c2c" stroke-width="1.4"/><path d="M9 6.5c-1.2.6-2 1.8-1.6 3.6.6 2.8 3 5.6 5.6 6.8 1.6.7 3 .2 3.6-.8l-1.8-1.8-1.5.8c-1.4-.7-2.6-2-3.2-3.4l.9-1.4z" fill="#2c2c2c"/></svg>
      <span>0000 000 000</span>
    </div>
    <div class="phone-row">
      <svg viewBox="0 0 24 24"><circle cx="12" cy="12" r="10.5" fill="none" stroke="#2c2c2c" stroke-width="1.4"/><rect x="8.5" y="5.5" width="7" height="13" rx="1.2" fill="none" stroke="#2c2c2c" stroke-width="1.4"/><rect x="10" y="7.5" width="4" height="4" fill="#2c2c2c"/></svg>
      <span>0000 000 000</span>
    </div>
  </div>
  <div class="phone-divider"></div>

  <div class="front-web">
    <div>Email: xxx@brindlereach.com.au</div>
    <div>Web: www.brindlereach.com.au</div>
  </div>

  <div class="front-brand">
    <div class="brand-dot"></div>
    <div class="brand-name">Brindle<br>Reach</div>
  </div>

  <div class="front-address">
    <svg viewBox="0 0 14 18"><path d="M7 0a6 6 0 0 0-6 6c0 4.5 6 12 6 12s6-7.5 6-12a6 6 0 0 0-6-6zm0 8.5A2.5 2.5 0 1 1 7 3.5a2.5 2.5 0 0 1 0 5z" fill="#828282"/></svg>
    <span>27 Calloway Street,&nbsp; Ashfield VIC 3148</span>
  </div>
</section>

<section class="card card-back" aria-label="Card back">
  <svg class="card-art" width="700" height="417" viewBox="0 0 700 417">
    <defs>
      <radialGradient id="back-dark" cx="0.45" cy="0.5" r="0.6">
        <stop offset="0" stop-color="#383838"/>
        <stop offset="1" stop-color="#151515"/>
      </radialGradient>
    </defs>
    <rect width="700" height="417" fill="url(#back-dark)"/>
    <path d="M575 0 Q655 18 700 70 L700 0 Z" fill="#8cc63f"/>
    <path d="M300 417 Q560 372 700 200 L700 417 Z" fill="#8cc63f"/>
  </svg>

  <div class="back-brand">
    <div class="brand-dot"></div>
    <div class="brand-name">Brindle<br>Reach</div>
  </div>
  <div class="back-slogan">Making You Visible</div>
  <div class="back-legal">Brindle Harbour Pty Ltd (ABN: 42 356 701 483)</div>
</section>

</body>
</html>
```